Business Card Design Project 4 Construction Business

I am after a creative, but sleek and simple/ clean business card design. This design will form the basis of future items and might include a logo or simply a creative way to lay out the text of my company name 'kestrel ventures'
I like the simplicity of black and white however I would also be happy to see a splash of colour introduced somehow to give the text some interest and make it stand out.
I would like a double sided card.
I am young (ish!) and professional, offering construction and project management services, what I don't want is the traditional builders type card featuring a cheesy hammer/ saw image etc.
As the company name, kestrel ventures, suggests, we focus on working closely and collaboratively together, in synergy with all stakeholders involved in the projects that we undertake
Construction

```html
<!DOCTYPE html>
<html lang="en">
<head>
<meta charset="utf-8">
<title>Kestrel Ventures – Business Card</title>
<link rel="stylesheet" href="https://fonts.googleapis.com/css2?family=Arimo:ital,wght@0,400;0,700;1,400&display=swap">
<style>
  :root {
    --page-bg: #e6e4e1;
    --card-black: #050505;
    --card-grad-top: #000000;
    --card-grad-bottom: #2b2b2b;
    --logo-grey: #8c8c8c;
    --logo-dark: #111111;
    --name-white: #ffffff;
    --detail-grey: #9a9a9a;
    --rule-light: #9c9c9c;
  }
  * { box-sizing: border-box; margin: 0; padding: 0; }
  html, body {
    width: 1200px; height: 1200px; overflow: hidden;
    background: var(--page-bg);
    font-family: "Arimo", Arial, sans-serif;
  }
  .card {
    position: absolute; left: 180px;
    width: 840px; height: 480px;
    box-shadow: 0 10px 30px rgba(0,0,0,0.25);
    overflow: hidden;
  }
  .card--logo-side { top: 80px; background: var(--card-black); }
  .card--info-side {
    top: 640px;
    background: linear-gradient(180deg, var(--card-grad-top) 0%, var(--card-grad-top) 25%, var(--card-grad-bottom) 100%);
  }
  .wordmark {
    position: absolute; left: 0; right: 0; text-align: center;
    font-weight: 700; line-height: 1;
  }
  .wordmark__main { display: block; font-size: 78px; letter-spacing: 2px; }
  .wordmark__sub { display: block; font-size: 36px; letter-spacing: 19px; margin-top: 6px; padding-left: 19px; }
  .card--logo-side .wordmark { top: 165px; color: var(--logo-grey); }
  .card--info-side .wordmark { top: 150px; color: var(--logo-dark); }
  .person { position: absolute; left: 50px; top: 38px; }
  .person__name { color: var(--name-white); font-weight: 700; font-size: 30px; }
  .person__role { color: var(--detail-grey); font-style: italic; font-size: 20px; margin-top: 4px; }
  .divider {
    position: absolute; left: 0; top: 300px; width: 100%; height: 2px;
    background: linear-gradient(90deg, var(--rule-light) 0%, var(--rule-light) 40%, rgba(156,156,156,0) 100%);
  }
  .contact {
    position: absolute; display: flex; align-items: center; gap: 10px;
    color: var(--detail-grey); font-weight: 700; font-size: 22px;
  }
  .contact svg { width: 22px; height: 22px; fill: var(--detail-grey); flex: none; }
  .contact--address { left: 50px; top: 320px; }
  .contact--mobile { left: 50px; top: 356px; }
  .contact--fax { left: 290px; top: 356px; }
  .contact--email { left: 500px; top: 420px; }
</style>
</head>
<body>
  <section class="card card--logo-side">
    <div class="wordmark">
      <span class="wordmark__main">KESTREL</span>
      <span class="wordmark__sub">VENTURES</span>
    </div>
  </section>

  <section class="card card--info-side">
    <div class="person">
      <div class="person__name">Owen Hartley</div>
      <div class="person__role">Director</div>
    </div>
    <div class="wordmark">
      <span class="wordmark__main">KESTREL</span>
      <span class="wordmark__sub">VENTURES</span>
    </div>
    <div class="divider"></div>

    <div class="contact contact--address">
      <svg viewBox="0 0 24 24" aria-hidden="true"><path d="M12 3 2 12h3v9h5v-6h4v6h5v-9h3z"/></svg>
      <span>Address line one</span>
    </div>
    <div class="contact contact--mobile">
      <svg viewBox="0 0 24 24" aria-hidden="true"><path d="M7 1h10a2 2 0 0 1 2 2v18a2 2 0 0 1-2 2H7a2 2 0 0 1-2-2V3a2 2 0 0 1 2-2zm0 3v14h10V4zm5 15.5a1.2 1.2 0 1 0 0 2.4 1.2 1.2 0 0 0 0-2.4z"/></svg>
      <span>123 456 789</span>
    </div>
    <div class="contact contact--fax">
      <svg viewBox="0 0 24 24" aria-hidden="true"><path d="M6 2h12v6H6zM3 9h18a1 1 0 0 1 1 1v8h-4v4H6v-4H2v-8a1 1 0 0 1 1-1zm5 8v3h8v-3z"/></svg>
      <span>123 456 789</span>
    </div>
    <div class="contact contact--email">
      <svg viewBox="0 0 24 24" aria-hidden="true"><path d="M2 5h20v14H2zm2 2v.5l8 5.5 8-5.5V7zm0 3v7h16v-7l-8 5.5z"/></svg>
      <span>info@kestrelventures.com</span>
    </div>
  </section>
</body>
</html>
```